Family Owned Construction Company Needs Modern Business Cards

We need a new design for our business cards. We are a family owned construction company, Torvane Construction, based in Mendon, Vermont and would like to add in our new logo and find a more modern look. We also want to use our old to make sure people know who we are. We do site development, highway, environmental, demolition, utility and aggregate.

Contact Information for Business Card

We want to have the office address, 48 Millbrook Road, Ashbury Falls, ME 04917 and our phone (802) 555-0148 and fax (802) 555-0193 on there as well. Our website is www.torvaneinc.example. There should be a place for the person's name, title, cell number, and email address on the card. Words that we would like to be associated with our company are honesty, predictable, reliable, integrity, dedicated, built right quality, consistent, whatever it takes, and innovation. Safety is also very important to us.

Font styles to use
Serif
Sans Serif
Other font styles liked:
• Square 721 Extented

Colors
0255a3
ffffff

Requirements
Must have
• Office address, phone number and fax number. New logo with excavator
Nice to have
• That we do site development, highway, environmental, demolition, utility, and aggregate. Both logos

```html
<!DOCTYPE html>
<html lang="en">
<head>
<meta charset="utf-8">
<title>Torvane Construction – Business Cards</title>
<link href="https://fonts.googleapis.com/css2?family=Open+Sans:wght@400;600;700;800&display=swap" rel="stylesheet">
<style>
  :root {
    --navy: #0a2c5e;
    --white: #ffffff;
    --ink: #1c1c1c;
    --backdrop: #e4e6ea;
    --edge: #d3d6db;
  }
  html, body {
    margin: 0;
    padding: 0;
    width: 1200px;
    height: 864px;
    overflow: hidden;
    background: var(--backdrop);
    font-family: "Open Sans", Arial, sans-serif;
  }
  .sheet {
    position: relative;
    width: 1200px;
    height: 864px;
  }
  .card {
    position: absolute;
    left: 310px;
    width: 580px;
    height: 332px;
    box-sizing: border-box;
    box-shadow: 0 4px 14px rgba(0,0,0,0.18);
  }
  .card--front {
    top: 72px;
    background: var(--navy);
    display: flex;
    align-items: center;
    justify-content: center;
  }
  .card--back {
    top: 460px;
    background: var(--white);
    border: 1px solid var(--edge);
  }
  .wordmark {
    font-weight: 800;
    text-transform: uppercase;
    letter-spacing: 0.02em;
    line-height: 1.05;
    margin: 0;
  }
  .card--front .wordmark {
    color: var(--white);
    font-size: 38px;
    text-align: center;
  }
  .card--back .wordmark {
    position: absolute;
    top: 34px;
    right: 40px;
    color: var(--navy);
    font-size: 28px;
    text-align: right;
  }
  .person {
    position: absolute;
    left: 44px;
    top: 104px;
  }
  .person__name {
    margin: 0;
    color: var(--navy);
    font-weight: 700;
    font-size: 19px;
  }
  .person__title {
    margin: 2px 0 0;
    color: var(--ink);
    font-size: 12px;
  }
  .contacts {
    position: absolute;
    right: 30px;
    bottom: 24px;
    margin: 0;
    padding: 0;
    list-style: none;
    text-align: right;
    color: var(--ink);
    font-size: 15px;
    line-height: 22px;
  }
  .contacts li {
    display: flex;
    justify-content: flex-end;
    align-items: center;
    gap: 9px;
  }
  .contacts svg {
    width: 12px;
    height: 12px;
    fill: var(--navy);
    flex: none;
  }
  .contacts .no-icon { padding-right: 21px; }
</style>
</head>
<body>
<main class="sheet">
  <section class="card card--front">
    <p class="wordmark">Torvane<br>Construction Inc.</p>
  </section>

  <section class="card card--back">
    <p class="wordmark">Torvane<br>Construction Inc.</p>

    <div class="person">
      <p class="person__name">Daniel Harlow</p>
      <p class="person__title">Managing Director</p>
    </div>

    <ul class="contacts">
      <li>(802) 555-0148
        <svg viewBox="0 0 12 12" aria-hidden="true"><path d="M2.5 1l2 2-1 1.3c.6 1.4 1.8 2.6 3.2 3.2L8 6.5l2 2-1.3 1.8C5 10 2 7 1.7 3.3z"/></svg>
      </li>
      <li>(802) 555-0172
        <svg viewBox="0 0 12 12" aria-hidden="true"><path d="M3 1h6v10H3zM4 2v7h4V2z"/></svg>
      </li>
      <li>(802) 555-0193
        <svg viewBox="0 0 12 12" aria-hidden="true"><path d="M3 1h5v3H3zM1 5h10v5H1zM3 8h6v3H3z"/></svg>
      </li>
      <li>info@torvaneinc.example
        <svg viewBox="0 0 12 12" aria-hidden="true"><path d="M1 3h10v7H1zM1.6 3.4L6 7l4.4-3.6"/></svg>
      </li>
      <li>www.torvaneinc.example
        <svg viewBox="0 0 12 12" aria-hidden="true"><circle cx="6" cy="6" r="5"/></svg>
      </li>
      <li class="no-icon">48 Millbrook Road, Ashbury Falls, ME 04917</li>
    </ul>
  </section>
</main>
</body>
</html>
```